Yard sign

I want it to look similar to this one,

change name to DRAVEK and submit new ideas

Also would like to improvise a bit. let's not make exactly the same thing

would like to change to: Connecticut #1 Company

also change phone to 203-555-0147
and website to
dravekllc.com

this is yard sign. size is 24' Width and 32' Height

Target Market(s)

Roof

Industry/Entity Type

Roofing

Requirements
Must have
• similar colors or add something new

```html
<!DOCTYPE html>
<html lang="en">
<head>
<meta charset="utf-8">
<title>DRAVEK Roofing Yard Sign</title>
<link rel="stylesheet" href="https://fonts.googleapis.com/css2?family=Barlow:wght@300;800;900&family=Barlow+Semi+Condensed:wght@800&family=Rubik:wght@500&display=swap">
<style>
  :root {
    --sign-yellow: #f6e112;
    --ink-black: #060607;
    --arrow-red: #e82127;
    --paper-white: #ffffff;
  }
  * { margin: 0; padding: 0; box-sizing: border-box; }
  html, body {
    width: 880px;
    height: 1200px;
    overflow: hidden;
    background: var(--sign-yellow);
  }
  .yard-sign {
    position: relative;
    width: 880px;
    height: 1200px;
    background: var(--sign-yellow);
    overflow: hidden;
  }
  .sign-graphics {
    position: absolute;
    inset: 0;
  }
  .headline {
    position: absolute;
    left: 0;
    width: 100%;
    text-align: center;
    color: var(--ink-black);
    line-height: 1;
  }
  .headline-region {
    top: 110px;
    left: 40px;
    font-family: "Barlow", sans-serif;
    font-weight: 300;
    font-size: 74px;
    letter-spacing: 2px;
    transform: rotate(-3deg);
  }
  .headline-rank {
    top: 185px;
    left: 40px;
    font-family: "Barlow", sans-serif;
    font-weight: 900;
    font-size: 96px;
    letter-spacing: -1px;
    transform: rotate(-3deg);
  }
  .brand-name {
    position: absolute;
    top: 300px;
    left: 0;
    width: 100%;
    text-align: center;
    font-family: "Barlow", sans-serif;
    font-weight: 900;
    font-size: 205px;
    line-height: 1;
    letter-spacing: -3px;
    color: var(--ink-black);
  }
  .phone-panel {
    position: absolute;
    left: 55px;
    top: 842px;
    width: 770px;
    height: 158px;
    background: var(--sign-yellow);
    display: flex;
    align-items: center;
    justify-content: center;
  }
  .phone-number {
    font-family: "Barlow Semi Condensed", sans-serif;
    font-weight: 800;
    font-size: 124px;
    line-height: 1;
    letter-spacing: 1px;
    color: var(--ink-black);
  }
  .web-address {
    position: absolute;
    top: 1022px;
    left: 0;
    width: 100%;
    text-align: center;
    font-family: "Rubik", sans-serif;
    font-weight: 500;
    font-size: 96px;
    line-height: 1;
    color: var(--paper-white);
  }
</style>
</head>
<body>
<main class="yard-sign">
  <svg class="sign-graphics" width="880" height="1200" viewBox="0 0 880 1200" aria-hidden="true">
    <polyline class="inner-frame" points="24,774 24,22 856,22 856,686"
              fill="none" stroke="var(--ink-black)" stroke-width="7"/>
    <polygon class="direction-arrow"
             points="49,637 499,595 486,542 838,590 506,704 502,642 53,688"
             fill="var(--arrow-red)" stroke="var(--ink-black)" stroke-width="6" stroke-linejoin="miter"/>
    <polygon class="contact-band" points="0,777 880,687 880,1200 0,1200" fill="var(--ink-black)"/>
  </svg>

  <p class="headline headline-region">Connecticut</p>
  <p class="headline headline-rank">#1 Company</p>
  <h1 class="brand-name">DRAVEK</h1>

  <div class="phone-panel">
    <p class="phone-number">203-555-0147</p>
  </div>
  <p class="web-address">dravekllc.com</p>
</main>
</body>
</html>
```